Computer consultant business card

Brimlo Software is a newly started computer consulting company. It's a small one-man company that provides mostly Velunix applications but also websites in collaboration with designers. I'm running this company on the side of full time university studies.

I want the final design to be clean and memorable. Be creative! :)

Some inspiration:
http://www.tavelpix.net/design/73519
http://www.tavelpix.net/design/2739566/business-card-design-by-quillbop
http://www.tavelpix.net/design/804613/business-card-design-by-lorvena-brukwaldsen

See attachment for my company logo.
Updates

I would like to thank everyone for submitting! I'll need a couple of days to review and ultimately select a design.

Target Market(s)

Non-technical entrepreneurs and small companies.

Industry/Entity Type

University

Requirements
Must have
• My company logo.
In any way, both colors from my logo.
First- and last name, e-mail and phone number.
Double-sided design.
Nice to have
• Something creative with the symbol in my logo

```html
<!DOCTYPE html>
<html lang="en">
<head>
<meta charset="utf-8">
<title>Brimlo Software Business Card</title>
<link href="https://fonts.googleapis.com/css2?family=Exo+2:wght@400;600;700&display=swap" rel="stylesheet">
<style>
  :root {
    --stage: #8d8f8e;
    --stage-light: #b4b5b4;
    --card-dark: #0d0d0e;
    --card-mid: #2a2b2d;
    --pill: #1c1d1f;
    --brand-blue: #2f6fd6;
    --text-light: #f2f2f2;
    --text-muted: #b9b9b9;
  }
  * { box-sizing: border-box; margin: 0; padding: 0; }
  html, body { width: 1200px; height: 861px; overflow: hidden; }
  body {
    background: radial-gradient(ellipse at 50% 35%, var(--stage-light), var(--stage));
    font-family: "Exo 2", sans-serif;
    position: relative;
  }
  .card {
    position: absolute;
    background: linear-gradient(160deg, var(--card-mid) 0%, var(--card-dark) 70%);
    border-radius: 4px;
    box-shadow: 0 18px 40px rgba(0,0,0,.45);
    overflow: hidden;
    color: var(--text-light);
  }
  .card-front { left: 190px; top: 140px; width: 360px; height: 580px; padding: 70px 34px 0; }
  .card-back { left: 610px; top: 250px; width: 520px; height: 320px; display: flex; align-items: center; justify-content: center; }

  .brand { display: flex; align-items: center; gap: 14px; }
  .brand-dot { width: 58px; height: 58px; border-radius: 50%; background: var(--brand-blue); flex: none; }
  .brand-name { font-weight: 600; font-size: 52px; line-height: 1; color: var(--text-light); }
  .card-back .brand-dot { width: 80px; height: 80px; }
  .card-back .brand-name { font-size: 90px; }

  .holder { margin-top: 66px; text-align: center; }
  .holder-name { font-weight: 700; font-size: 31px; line-height: 1.05; }
  .holder-role { font-size: 17px; color: var(--text-muted); letter-spacing: .5px; }

  .contacts { list-style: none; margin-top: 34px; display: flex; flex-direction: column; gap: 18px; }
  .contact {
    display: flex; align-items: center; gap: 16px;
    height: 46px; padding: 0 16px;
    background: var(--pill); border-radius: 23px;
    font-size: 19px; color: var(--text-light);
    box-shadow: inset 0 1px 0 rgba(255,255,255,.06);
  }
  .contact svg { width: 22px; height: 22px; flex: none; fill: var(--text-light); }
</style>
</head>
<body>

<section class="card card-front" role="img" aria-label="Front of business card on dark perforated metal texture">
  <div class="brand">
    <span class="brand-dot"></span>
    <span class="brand-name">brimlo</span>
  </div>
  <div class="holder">
    <p class="holder-name">Name Surname</p>
    <p class="holder-role">Position</p>
  </div>
  <ul class="contacts">
    <li class="contact">
      <svg viewBox="0 0 24 24"><path d="M6.6 10.8a15 15 0 0 0 6.6 6.6l2.2-2.2a1 1 0 0 1 1-.25 11.4 11.4 0 0 0 3.6.57 1 1 0 0 1 1 1V20a1 1 0 0 1-1 1A17 17 0 0 1 3 4a1 1 0 0 1 1-1h3.5a1 1 0 0 1 1 1c0 1.25.2 2.45.57 3.57a1 1 0 0 1-.25 1z"/></svg>
      <span>+1555-0142-7300</span>
    </li>
    <li class="contact">
      <svg viewBox="0 0 24 24"><path d="M2 5h20v14H2z M3.5 6.5 12 13l8.5-6.5" fill="none" stroke="#f2f2f2" stroke-width="1.8"/></svg>
      <span>name@brimlosoft.com</span>
    </li>
    <li class="contact">
      <svg viewBox="0 0 24 24"><g fill="none" stroke="#f2f2f2" stroke-width="1.6"><circle cx="12" cy="12" r="9.5"/><ellipse cx="12" cy="12" rx="4" ry="9.5"/><path d="M2.5 12h19M4 7h16M4 17h16"/></g></svg>
      <span>www.brimlosoft.net</span>
    </li>
  </ul>
</section>

<section class="card card-back" role="img" aria-label="Back of business card on dark perforated metal texture">
  <div class="brand">
    <span class="brand-dot"></span>
    <span class="brand-name">brimlo</span>
  </div>
</section>

</body>
</html>
```